Varnow Renewables Inc. Website

Design website. Solar & Renewables company little background functionality HTML based cross-platform compliant. The company name is Varnow Renewables Inc. a grid-Tied and off-grid professional design and installation company. Trelisk certified installations. Also a certified sales and service dealer for Polvane Generators.

Target Market(s)

General Contractors, Big Contracts, Commercial

Industry/Entity Type

Solar Energy

Coding

Coded - Design and coding required

Number of Pages Required

4 page

Requirements
Must have
• A Simple navigation link for a few pages. 1) Home page - company images and trelisk certifaction seal. 2) Polvane Generators Sales & Service Dealer Page 3) Off Grid Solutions Page highlighting having your home off grid 4) GRid-Tied Installations for installing solar while your home is connected to the utility lines
Nice to have
• Links to some brands typically installed. KORtrix, Mirvolt, Zandus, TV, Hestor, Pellard, Etc., Could seperate the brands on what they offer if off grid materials or grid tied.
Should not have
• Do not need to showcase previous projects.

```html
<!DOCTYPE html>
<html lang="en">
<head>
<meta charset="utf-8">
<title>Varnow Renewables Inc.</title>
<link href="https://fonts.googleapis.com/css2?family=Montserrat:wght@500;600;700&family=Roboto:wght@300;400;500&display=swap" rel="stylesheet">
<style>
:root{
  --orange:#f68b1f;
  --ink:#222222;
  --brand-ink:#2d3a4f;
  --muted:#666666;
  --footer:#2a2a2a;
  --white:#ffffff;
  --card-line:#e4e4e4;
}
*{box-sizing:border-box;margin:0;padding:0}
html,body{width:1200px;height:2990px;overflow:hidden}
body{position:relative;background:var(--white);font-family:'Roboto',sans-serif;color:var(--ink)}
.abs{position:absolute}

/* hero */
.hero{left:0;top:0;width:1200px;height:640px;overflow:hidden;
  background:linear-gradient(180deg,#3b2f2e 0%,#7a4a2e 22%,#b8693a 40%,#6b3a22 55%,#c9733a 72%,#e08d48 86%,#7a4125 100%)}
.logo{left:114px;top:36px;color:var(--white)}
.logo-name{font-family:'Montserrat',sans-serif;font-weight:500;font-size:40px;letter-spacing:3px;line-height:1}
.logo-sub{font-family:'Montserrat',sans-serif;font-weight:500;font-size:16px;letter-spacing:2px;margin-top:2px}
.nav{right:113px;top:58px;display:flex;gap:37px;list-style:none}
.nav li{font-size:16px;color:var(--white);letter-spacing:.3px}
.nav li.active{color:var(--orange)}
.hero-title{left:0;width:1200px;top:268px;text-align:center;color:var(--white);
  font-family:'Montserrat',sans-serif;font-weight:600;font-size:60px;line-height:72px}
.arrow{top:298px;width:24px;height:30px}
.hero-curve{left:0;top:540px;width:1200px;height:100px}

/* who we are */
.section-title{left:0;width:1200px;text-align:center;font-family:'Montserrat',sans-serif;font-weight:600}
.who-title{top:728px;font-size:40px;color:var(--ink)}
.who-text{left:113px;width:974px;top:796px;text-align:center;font-weight:300;font-size:16px;line-height:34px;color:var(--muted)}
.btn-more{left:523px;top:951px;width:154px;height:50px;border-radius:25px;background:var(--orange);color:var(--white);
  font-size:16px;display:flex;align-items:center;justify-content:center;box-shadow:0 2px 4px rgba(0,0,0,.2)}

/* services */
.services{left:0;top:1102px;width:1200px;height:548px;background:linear-gradient(180deg,#161514 0%,#2a221d 50%,#1b1816 100%)}
.services-title{top:42px;font-size:42px;color:var(--white)}
.service{top:116px;width:340px;text-align:center;color:var(--white)}
.service-photo{position:relative;width:290px;height:290px;border-radius:50%;margin:0 auto;overflow:hidden}
.service-tag{position:absolute;left:35px;top:204px;width:220px;height:200px;border-radius:50%;background:rgba(246,139,31,.85);
  padding-top:18px;font-size:16px;line-height:23px}
.service-head{margin-top:18px;font-weight:500;font-size:21px;letter-spacing:.3px}
.service-text{margin-top:10px;font-size:13.5px;font-weight:300;line-height:26px}

/* brands */
.brands-title{top:1742px;font-size:42px;color:var(--orange)}
.brands-sub{left:0;width:1200px;top:1798px;text-align:center;font-size:16px;color:var(--ink)}
.brand-card{top:1851px;width:237px;height:258px;border:2px solid var(--card-line);border-radius:6px;text-align:center;background:var(--white)}
.brand-name{height:72px;margin-top:18px;display:flex;align-items:center;justify-content:center;
  font-family:'Montserrat',sans-serif;font-weight:600;font-size:24px;color:var(--brand-ink)}
.brand-text{padding:0 8px;font-size:13.5px;font-weight:300;line-height:26px;color:var(--muted)}

/* contact */
.map{left:0;top:2212px;width:600px;height:552px;background:linear-gradient(135deg,#f1f1f3 0%,#e9e9ec 60%,#f3f3f5 100%)}
.contact-panel{left:600px;top:2212px;width:600px;height:552px;background:var(--orange)}
.contact-title{left:665px;top:2260px;font-family:'Montserrat',sans-serif;font-weight:600;font-size:42px;color:var(--white)}
.field{height:51px;border:1px solid var(--white);color:var(--white);font-size:16px;padding:16px 6px 0}
.submit{left:671px;top:2660px;width:429px;height:49px;background:#000;color:var(--white);font-size:15px;font-weight:500;
  display:flex;align-items:center;justify-content:center;letter-spacing:.5px}

/* footer */
.footer{left:0;top:2764px;width:1200px;height:226px;background:var(--footer);color:var(--white)}
.footer-nav{left:0;width:1200px;top:60px;display:flex;justify-content:center;gap:69px;list-style:none;font-size:16px}
.footer-info{left:0;width:1200px;top:103px;display:flex;justify-content:center;gap:76px;font-size:16px}
.footer-info span{display:flex;align-items:center;gap:8px}
.copyright{left:505px;top:178px;font-size:16px}
.partner-box{left:115px;top:168px;width:78px;height:50px;background:#111}
.partner-name{left:222px;top:176px;font-weight:500;font-size:20px;color:var(--orange)}
.partner-seal{left:367px;top:164px;width:58px;height:58px;border-radius:50%;background:#f0a12c}
.social{top:190px;width:16px;height:16px;border-radius:50%;background:var(--white)}
</style>
</head>
<body>

<header class="hero abs" role="img" aria-label="Solar panel field and wind turbines at sunset"></header>
<div class="logo abs">
  <div class="logo-name">VARNOW</div>
  <div class="logo-sub">RENEWABLES</div>
</div>
<ul class="nav abs">
  <li class="active">HOME</li><li>OUR PRODUCTS</li><li>OUR BRANDS</li><li>ABOUT</li><li>CONTACT</li>
</ul>
<h1 class="hero-title abs">WELCOME TO VARNOW<br>RENEWABLES INC</h1>
<svg class="arrow abs" style="left:92px" viewBox="0 0 24 30"><path d="M16 4 L6 15 L16 26" fill="none" stroke="#fff" stroke-width="3"/></svg>
<svg class="arrow abs" style="left:1088px" viewBox="0 0 24 30"><path d="M8 4 L18 15 L8 26" fill="none" stroke="#fff" stroke-width="3"/></svg>
<svg class="hero-curve abs" viewBox="0 0 1200 100" preserveAspectRatio="none">
  <path d="M0 20 Q600 150 1200 20 L1200 100 L0 100 Z" fill="#fff"/>
  <path d="M0 20 Q600 150 1200 20" fill="none" stroke="#f68b1f" stroke-width="7"/>
</svg>

<h2 class="section-title who-title abs">WHO WE ARE</h2>
<p class="who-text abs">Varnow Renewables Inc. is an Ridgeview based solar installer of both grid-tied and off-grid PV solutions. Installations are carry out by certified electrical experts. We only install the best equipment, backed by the most secure warranty on the market today. We only offer our customers the highest quality products available on the market - and for the best prices you’ll find anywhere. Want to know more?<br>Get in touch with our team today.</p>
<div class="btn-more abs">READ MORE</div>

<section class="services abs">
  <h2 class="section-title services-title abs">SERVICES WE OFFER</h2>
  <div class="service abs" style="left:86px">
    <div class="service-photo" role="img" aria-label="Sunlight through tree branches" style="background:radial-gradient(circle at 35% 30%,#fffbe6 0%,#c9d27a 25%,#6f8a3a 55%,#3c4a22 100%)">
      <div class="service-tag">Free Estimates &amp;<br>Consults!</div>
    </div>
    <div class="service-head">FEEL THE POWER!</div>
    <div class="service-text">Unleash your PV potential. Our clients always<br>say "I should have done this sooner"</div>
  </div>
  <div class="service abs" style="left:430px">
    <div class="service-photo" role="img" aria-label="Glowing light bulbs in the dark" style="background:radial-gradient(circle at 30% 35%,#f2b25a 0%,#a5561e 30%,#3a1c0c 70%,#1d0f07 100%)">
      <div class="service-tag">Grid-Tied Solutions</div>
    </div>
    <div class="service-head">TRUSTY &amp; RELIABLE</div>
    <div class="service-text">Reduce your monthly electrical bills by feeding<br>your solar energy back into your local grid.</div>
  </div>
  <div class="service abs" style="left:772px">
    <div class="service-photo" role="img" aria-label="Aerial view of solar panel rows" style="background:linear-gradient(135deg,#2b3a7a 0%,#3a4f8e 45%,#3c6e3a 70%,#28427a 100%)">
      <div class="service-tag">Off-Grid Installations</div>
    </div>
    <div class="service-head">FEEL EMPOWERED!</div>
    <div class="service-text">Enjoy clean, quiet and tranquil electricity while<br>keeping your solitude and independence.</div>
  </div>
</section>

<h2 class="section-title brands-title abs">TOP-QUALITY BRANDS</h2>
<p class="brands-sub abs">Names You Can Trust with a warranty you feel comfortable with.</p>
<div class="brand-card abs" style="left:113px">
  <div class="brand-name">Halvern PV</div>
  <p class="brand-text">Halvern PV is dedicated to helping Canadians use solar electricity in their homes and businesses. With over 30 years of experience,country and can ensure your project</p>
</div>
<div class="brand-card abs" style="left:359px">
  <div class="brand-name">TV</div>
  <p class="brand-text">TV provides solar products with industry leading power outputs. The DNA of TV’s innovation continue to serve as the driving force for TV’s leadership of the solar energy</p>
</div>
<div class="brand-card abs" style="left:605px">
  <div class="brand-name">Zandus</div>
  <p class="brand-text">Zandus manufacturers solar cells and modules and is the premier product brand of Zandus. solar modules are Germany and meet the highest quality standards</p>
</div>
<div class="brand-card abs" style="left:851px">
  <div class="brand-name" style="font-size:21px">Northmere Solar</div>
  <p class="brand-text">Customers choose us because we deliver the best-possible value. Our modules and system solutions combine superior market-leading cost structures.</p>
</div>

<div class="map abs" role="img" aria-label="Street map showing the office location on Larchmont Road"></div>
<div class="contact-panel abs"></div>
<h2 class="contact-title abs">CONTACT</h2>
<div class="field abs" style="left:671px;top:2328px;width:211px">Name</div>
<div class="field abs" style="left:889px;top:2328px;width:211px">Email</div>
<div class="field abs" style="left:671px;top:2400px;width:211px">Phone</div>
<div class="field abs" style="left:889px;top:2400px;width:211px">Address</div>
<div class="field abs" style="left:671px;top:2472px;width:429px">Subject</div>
<div class="field abs" style="left:671px;top:2541px;width:429px;height:103px">Type your message here</div>
<div class="submit abs">SUBMIT</div>

<footer class="footer abs">
  <ul class="footer-nav abs"><li>HOME</li><li>OUR PRODUCTS</li><li>OUR BRANDS</li><li>ABOUT</li><li>CONTACT</li></ul>
  <div class="footer-info abs">
    <span><svg width="10" height="14" viewBox="0 0 10 14"><path d="M5 0a5 5 0 0 0-5 5c0 4 5 9 5 9s5-5 5-9a5 5 0 0 0-5-5zm0 7a2 2 0 1 1 0-4 2 2 0 0 1 0 4z" fill="#f68b1f"/></svg>418 Larchmont Road, Ridgeview B.C.</span>
    <span><svg width="14" height="14" viewBox="0 0 14 14"><path d="M3 1l2.5 3-1.5 1.5c1 2 2.5 3.5 4.5 4.5L10 8.5 13 11l-1.5 2.5C6 13 1 8 .5 2.5z" fill="#f68b1f"/></svg>555.214.3090</span>
    <span><svg width="16" height="12" viewBox="0 0 16 12"><rect x="1" y="1" width="14" height="10" fill="none" stroke="#f68b1f" stroke-width="1.5"/><path d="M1 1l7 6 7-6" fill="none" stroke="#f68b1f" stroke-width="1.5"/></svg>info@varnowrenewables.com</span>
  </div>
  <div class="partner-box abs"></div>
  <div class="partner-name abs">Polvane</div>
  <div class="partner-seal abs"></div>
  <div class="copyright abs">© 2020 All Rights Reserved</div>
  <div class="social abs" style="left:1020px"></div>
  <div class="social abs" style="left:1043px"></div>
  <div class="social abs" style="left:1066px"></div>
</footer>

</body>
</html>
```